Need a business card for our overland brand!

We had the logo made and we need a great design for our business card. Use the logo provide or tweak it however you see fit.

Contact Information for Business Card

Name, Title, Telephone, email, website

```html
<!DOCTYPE html>
<html lang="en">
<head>
<meta charset="utf-8">
<title>Summit Trailworks – Business Card</title>
<link href="https://fonts.googleapis.com/css2?family=Montserrat:wght@500;700;800&display=swap" rel="stylesheet">
<style>
  :root {
    --backdrop: #232323;
    --brand-blue: #03a4cb;
    --ink: #050505;
    --paper: #ffffff;
    --muted: #222222;
  }
  html, body {
    margin: 0;
    width: 1200px;
    height: 901px;
    overflow: hidden;
    background: var(--backdrop);
    font-family: "Montserrat", Arial, sans-serif;
  }
  .card {
    position: absolute;
    left: 320px;
    width: 560px;
    height: 320px;
    border-radius: 18px;
    overflow: hidden;
  }
  .card-front {
    top: 100px;
    background: var(--brand-blue);
    display: flex;
    align-items: center;
    justify-content: center;
  }
  .brand {
    display: flex;
    align-items: center;
    gap: 14px;
    color: var(--paper);
    font-weight: 800;
    text-transform: uppercase;
    letter-spacing: 1px;
  }
  .brand-dot {
    width: 58px;
    height: 58px;
    border-radius: 50%;
    background: var(--paper);
  }
  .brand-name {
    font-size: 34px;
    line-height: 1.02;
  }
  .card-back {
    top: 470px;
    background: var(--paper);
  }
  .scenery {
    position: absolute;
    left: 0;
    right: 0;
    top: 110px;
    bottom: 0;
    background: linear-gradient(180deg, var(--brand-blue) 0%, var(--ink) 38%, var(--ink) 100%);
  }
  .holder {
    position: absolute;
    top: 34px;
    right: 34px;
    text-align: right;
  }
  .holder-name {
    margin: 0;
    color: var(--brand-blue);
    font-weight: 800;
    font-size: 21px;
    text-transform: uppercase;
  }
  .holder-title {
    margin: 2px 0 0;
    color: var(--muted);
    font-weight: 500;
    font-size: 14px;
  }
  .contact {
    position: absolute;
    left: 34px;
    bottom: 26px;
    color: var(--paper);
    font-size: 15px;
    font-weight: 500;
    line-height: 1.35;
  }
  .address { margin: 0 0 12px; }
  .contact-list { list-style: none; margin: 0; padding: 0; }
  .contact-list li { display: flex; align-items: center; gap: 10px; }
  .contact-list svg { width: 14px; height: 14px; fill: var(--brand-blue); flex: none; }
  .card-back .brand {
    position: absolute;
    right: 30px;
    bottom: 52px;
    gap: 9px;
  }
  .card-back .brand-dot { width: 34px; height: 34px; background: var(--brand-blue); }
  .card-back .brand-name { font-size: 19px; }
</style>
</head>
<body>

<section class="card card-front">
  <div class="brand">
    <span class="brand-dot"></span>
    <span class="brand-name">Summit<br>Trailworks</span>
  </div>
</section>

<section class="card card-back">
  <div class="scenery" role="img" aria-label="Mountain range silhouette in black with blue outlined peaks"></div>

  <div class="holder">
    <p class="holder-name">Dana Whitfield</p>
    <p class="holder-title">President</p>
  </div>

  <div class="contact">
    <p class="address">Ridge Ave 027, Suite 210<br>State CO, Zip 00027, USA</p>
    <ul class="contact-list">
      <li><svg viewBox="0 0 24 24"><path d="M6.6 10.8a15 15 0 0 0 6.6 6.6l2.2-2.2c.3-.3.7-.4 1-.2 1.1.4 2.3.6 3.6.6.6 0 1 .4 1 1V20c0 .6-.4 1-1 1A17 17 0 0 1 3 4c0-.6.4-1 1-1h3.5c.6 0 1 .4 1 1 0 1.3.2 2.5.6 3.6.1.3 0 .7-.2 1z"/></svg>014-555-0182</li>
      <li><svg viewBox="0 0 24 24"><path d="M2 5h20v14H2zm2 2v.5l8 5 8-5V7l-8 5z"/></svg>hello@summittrail.com</li>
      <li><svg viewBox="0 0 24 24"><path d="M12 2a10 10 0 1 0 0 20 10 10 0 0 0 0-20zm6.9 6h-3a15 15 0 0 0-1.3-4 8 8 0 0 1 4.3 4zM12 4c.8 1.2 1.5 2.5 1.9 4h-3.8c.4-1.5 1.1-2.8 1.9-4zM4.3 14a8 8 0 0 1 0-4h3.4a16 16 0 0 0 0 4zm.8 2h3a15 15 0 0 0 1.3 4 8 8 0 0 1-4.3-4zm3-8h-3a8 8 0 0 1 4.3-4 15 15 0 0 0-1.3 4zM12 20c-.8-1.2-1.5-2.5-1.9-4h3.8c-.4 1.5-1.1 2.8-1.9 4zm2.3-6H9.7a14 14 0 0 1 0-4h4.6a14 14 0 0 1 0 4zm.3 5.6a15 15 0 0 0 1.3-3.6h3a8 8 0 0 1-4.3 3.6zm1.7-5.6a16 16 0 0 0 0-4h3.4a8 8 0 0 1 0 4z"/></svg>summittrail.com</li>
    </ul>
  </div>

  <div class="brand">
    <span class="brand-dot"></span>
    <span class="brand-name">Summit<br>Trailworks</span>
  </div>
</section>

</body>
</html>
```